依頼詳細
デザイン住宅の看板デザインをお願いします。
生活道路沿いの路上看板のデザインになります。
事務所上の看板デザインに沿って頂き、シンプルで目立つ看板のデザインでお願いします。
記載項目
会社名:株式会社キリノハコビヤ
電話番号:0574-83-5167
ロゴ(添付ファイル)
看板写真(添付ファイル:宮鶴屋さんの下部分になります)
参考:事務所上の看板(添付ファイル)
希望イメージ
希望する色
水色系、無彩色系
納品ファイル
• 高解像度JPG (.jpg)
• イラストレーター形式 (.ai)
• フォトショップ形式 (.psd)
• PNG形式 (.png)
補足説明
〇想い
高性能でカッコいい家をどこよりもお値打ちに
家づくりは楽しくなくてはならない
家族みんなが毎日笑顔になるオリジナルの家
想いをカタチにできる家
地震に強く、高性能は当たり前

〇メインターゲット
子育て世代・共働き世代
大手ハウスメーカー層から降りてこられるお客様
デザイン住宅(設計事務所)から降りてこられるお客様
看板サイズ 幅1350mm×高さ2500mm

看板の位置の写真の追加させて頂きます。
■ 選んだ理由

シンプルさの中に、親しみを一番感じました。
優しいコントラストの中に、温かみも含まれてると感じ、
こちらのご提案を採用させて頂きました。

■ 提案者全員のお礼・コメント

たくさんのご提案を頂き、ありがとうございました!
正直こんなにご提案頂けるとは思っておらず、
皆さまのデザインに対する想いがすごく伝わり、とても勉強になりました。
次の機会があれば、またご依頼させて頂きたいと思います。
ありがとうございました!

```html
<!DOCTYPE html>
<html lang="ja">
<head>
<meta charset="utf-8">
<title>キリノハコビヤ 路上看板</title>
<link rel="stylesheet" href="https://fonts.googleapis.com/css2?family=Noto+Sans+JP:wght@400;500;700&family=Cormorant+Garamond:wght@500&display=swap">
<style>
  :root {
    --navy: #1f2a44;
    --navy-line: #2b3857;
    --paper: #ffffff;
    --ink: #2a2a2a;
    --frame: #b9b9b9;
  }
  html, body {
    margin: 0;
    padding: 0;
    overflow: hidden;
    background: var(--paper);
  }
  .signboard {
    position: relative;
    width: 711px;
    height: 1200px;
    box-sizing: border-box;
    border: 2px solid var(--frame);
    background: var(--paper);
    overflow: hidden;
  }
  .hero {
    position: absolute;
    left: 69px;
    top: 67px;
    width: 573px;
    height: 759px;
    background:
      repeating-linear-gradient(90deg,
        var(--navy) 0 7px,
        var(--navy-line) 7px 9px);
    clip-path: polygon(0 0, 100% 0, 100% 100%, 50% 667px, 0 100%);
  }
  .catchcopy {
    position: absolute;
    top: 60px;
    right: 60px;
    margin: 0;
    writing-mode: vertical-rl;
    font-family: "Noto Sans JP", sans-serif;
    font-weight: 500;
    font-size: 82px;
    line-height: 115px;
    letter-spacing: 0.02em;
    color: var(--paper);
  }
  .catchcopy span { display: block; }
  .brand {
    position: absolute;
    left: 0;
    width: 100%;
    top: 850px;
    text-align: center;
    font-family: "Cormorant Garamond", serif;
    font-weight: 500;
    font-size: 56px;
    letter-spacing: 0.04em;
    color: var(--ink);
    line-height: 1;
  }
  .contact {
    position: absolute;
    left: 0;
    width: 100%;
    top: 990px;
    text-align: center;
    color: var(--ink);
    font-family: "Noto Sans JP", sans-serif;
  }
  .tel {
    margin: 0;
    font-size: 40px;
    font-weight: 400;
    letter-spacing: 0.04em;
    line-height: 1.2;
  }
  .tel-label { font-size: 34px; margin-right: 6px; }
  .company {
    margin: 14px 0 0;
    font-size: 21px;
    font-weight: 700;
    letter-spacing: 0.02em;
  }
</style>
</head>
<body>
  <main class="signboard">
    <section class="hero">
      <h1 class="catchcopy">
        <span>高性能で</span>
        <span>かっこいい家を</span>
        <span>お値打ちで</span>
        <span>建てます</span>
      </h1>
    </section>
    <div class="brand">KIRINO HAKOBIYA</div>
    <footer class="contact">
      <p class="tel"><span class="tel-label">TEL.</span>0574-83-5167</p>
      <p class="company">株式会社キリノハコビヤ</p>
    </footer>
  </main>
</body>
</html>
```